Real Estate Card Design

I need a new business card! Below you will find my headshot, the company logo and a copy of my previous business card.

The card must contain the following information:

Dana Welch
Sales Representative
FAIR HARBOUR HOMES REALTY INC BROKERGE
204-517 Maple Ave E, Oshawa ON L1G 4K7
Cell: 905-618-4037 Office:905-481-2696
www.danawelch.com dana@movewithwelch.ca

I would like the card to portray security and class all the while being fresh and contemporary. I hold the key....

```html
<!DOCTYPE html>
<html lang="en">
<head>
<meta charset="utf-8">
<title>Dana Welch – Business Card</title>
<link href="https://fonts.googleapis.com/css2?family=Libre+Baskerville:wght@700&family=PT+Sans:wght@400;700&display=swap" rel="stylesheet">
<style>
  :root {
    --blue: #1f9ad6;
    --ink: #0c1212;
    --paper: #f4f5f5;
    --white: #ffffff;
    --stage: #d9dbdc;
  }
  * { margin: 0; padding: 0; box-sizing: border-box; }
  html, body { width: 1200px; height: 1021px; overflow: hidden; }
  body {
    background: var(--stage);
    font-family: "PT Sans", sans-serif;
    position: relative;
  }
  .card {
    position: absolute;
    left: 200px;
    width: 800px;
    height: 457px;
    overflow: hidden;
    box-shadow: 0 6px 18px rgba(0,0,0,.25);
  }
  .card--front { top: 30px; background: var(--paper); }
  .card--back { top: 534px; background: var(--ink); color: var(--white); }

  /* brand lockup */
  .brand { position: absolute; text-align: center; }
  .brand__square { display: block; margin: 0 auto; background: var(--blue); }
  .brand__name {
    display: block;
    font-family: "PT Sans", sans-serif;
    font-weight: 700;
    letter-spacing: .04em;
    line-height: 1.15;
    white-space: nowrap;
  }
  .brand__rule { display: block; height: 3px; background: var(--blue); margin: 6px auto 0; }

  .card--front .brand { left: 0; right: 0; top: 120px; }
  .card--front .brand__square { width: 120px; height: 110px; }
  .card--front .brand__name { color: var(--ink); font-size: 30px; margin-top: 14px; }
  .card--front .brand__name small { display: block; font-size: 15px; letter-spacing: .3em; }
  .card--front .brand__rule { width: 420px; }

  .card--back .brand { left: 150px; width: 300px; top: 30px; }
  .card--back .brand__square { width: 88px; height: 80px; }
  .card--back .brand__name { color: var(--white); font-size: 21px; margin-top: 10px; }
  .card--back .brand__name small { display: block; font-size: 11px; letter-spacing: .3em; }
  .card--back .brand__rule { width: 280px; }

  .portrait {
    position: absolute;
    right: 0; top: 0;
    width: 250px; height: 439px;
    background: radial-gradient(ellipse at 55% 40%, #5a4a3c 0%, #2a2522 35%, #141619 70%, var(--ink) 100%);
  }

  .agent { position: absolute; left: 60px; top: 218px; white-space: nowrap; }
  .agent__name {
    font-family: "Libre Baskerville", serif;
    font-weight: 700;
    color: var(--blue);
    font-size: 22px;
    letter-spacing: .02em;
  }
  .agent__title { font-size: 19px; margin-top: 4px; }

  .website { position: absolute; left: 60px; top: 332px; font-size: 19px; white-space: nowrap; }
  .website em { font-style: normal; color: var(--blue); }

  .divider { position: absolute; left: 290px; top: 232px; width: 2px; height: 168px; background: var(--blue); }

  .contact { position: absolute; left: 310px; top: 236px; font-size: 17px; line-height: 1.3; white-space: nowrap; }
  .contact__address { margin-bottom: 12px; }
  .contact__row { display: flex; align-items: center; gap: 8px; }
  .contact__row svg { width: 15px; height: 15px; flex: none; }

  .band { position: absolute; left: 0; right: 0; bottom: 0; height: 18px; background: var(--blue); }
</style>
</head>
<body>

<section class="card card--front" aria-label="Card front">
  <div class="brand">
    <span class="brand__square"></span>
    <span class="brand__name">FAIR HARBOUR HOMES<small>REALTY INC BROKERGE</small></span>
    <span class="brand__rule"></span>
  </div>
</section>

<section class="card card--back" aria-label="Card back">
  <div class="portrait" role="img" aria-label="Headshot of Dana Welch in a pinstripe blazer holding up a house key"></div>

  <div class="brand">
    <span class="brand__square"></span>
    <span class="brand__name">FAIR HARBOUR HOMES<small>REALTY INC BROKERGE</small></span>
    <span class="brand__rule"></span>
  </div>

  <div class="agent">
    <div class="agent__name">DANA WELCH</div>
    <div class="agent__title">Sales Representative</div>
  </div>

  <div class="website">www.<em>danawelch</em>.com</div>

  <div class="divider"></div>

  <div class="contact">
    <div class="contact__address">204-517 Maple Ave E<br>Oshawa ON L1G 4K7</div>
    <div class="contact__row">
      <svg viewBox="0 0 16 16" fill="none" stroke="#1f9ad6" stroke-width="1.6"><rect x="4" y="1" width="8" height="14" rx="1.5"/><line x1="7" y1="12.5" x2="9" y2="12.5"/></svg>
      905-618-4037
    </div>
    <div class="contact__row">
      <svg viewBox="0 0 16 16" fill="#1f9ad6"><path d="M3.5 1l3 3-1.7 2a9 9 0 0 0 5.2 5.2l2-1.7 3 3-2 2.3C7 14.5 1.5 9 1.2 3z"/></svg>
      905-481-2696
    </div>
    <div class="contact__row">
      <svg viewBox="0 0 16 16" fill="none" stroke="#1f9ad6" stroke-width="1.6"><rect x="1" y="3" width="14" height="10"/><polyline points="1,3 8,9 15,3"/></svg>
      dana@movewithwelch.ca
    </div>
  </div>

  <div class="band"></div>
</section>

</body>
</html>
```